Business Card Design for a Personal Trainer

I need a business card design for my job as a personal trainer. It should have a unique, modern and exclusive design. On the front there should be only my logo with my name and my job. 0163/2918374 Tobias Kellinger Lindenfeldweg 14 80412 Munich Germany The most important contact information is the web adress. it can be bigger than the rest, but its not necessary. The card should be 8,5cmx5,5cm big. Font: Roboto. Colors: black, white, gray, 56c1ff.

```html
<!DOCTYPE html>
<html lang="de">
<head>
<meta charset="utf-8">
<title>Tobias Kellinger – Visitenkarte</title>
<link rel="stylesheet" href="https://fonts.googleapis.com/css2?family=Roboto:wght@300;400;500&display=swap">
<style>
  :root {
    --bg: #1f1f1f;
    --black: #050505;
    --white: #f4f4f4;
    --card-light: #eeeeef;
    --card-light-2: #dcdde0;
    --ink: #111111;
    --photo-a: #cfd0d3;
    --photo-b: #4a4a4c;
  }
  * { margin: 0; padding: 0; box-sizing: border-box; }
  html, body { width: 1200px; height: 1200px; overflow: hidden; }
  body {
    background: var(--bg);
    font-family: "Roboto", Arial, sans-serif;
    position: relative;
  }
  .card {
    position: absolute;
    left: 220px;
    width: 760px;
    height: 492px;
    overflow: hidden;
  }
  /* Front */
  .card--front {
    top: 88px;
    background: var(--black);
    color: var(--white);
    display: flex;
    flex-direction: column;
    align-items: center;
    justify-content: center;
  }
  .brand-mark {
    width: 34px; height: 34px;
    background: var(--white);
    margin-bottom: 30px;
  }
  .brand-name {
    font-weight: 400;
    font-size: 58px;
    letter-spacing: 2px;
    text-transform: uppercase;
    line-height: 1;
  }
  .brand-role {
    display: flex;
    align-items: center;
    gap: 14px;
    margin-top: 8px;
    font-weight: 400;
    font-size: 22px;
    letter-spacing: 7px;
    text-transform: uppercase;
  }
  .brand-role::before, .brand-role::after {
    content: "";
    width: 90px; height: 2px;
    background: var(--white);
  }
  /* Back */
  .card--back {
    top: 620px;
    background: linear-gradient(120deg, var(--card-light) 0%, var(--card-light-2) 100%);
    color: var(--ink);
  }
  .contact-list {
    position: absolute;
    left: 40px; top: 100px;
    list-style: none;
    z-index: 1;
  }
  .contact-item {
    display: flex;
    align-items: center;
    height: 60px;
    font-size: 25px;
    font-weight: 400;
    white-space: nowrap;
  }
  .contact-item svg {
    width: 34px; height: 34px;
    margin-right: 36px;
    fill: var(--ink);
    flex: none;
  }
  .web-band {
    position: absolute;
    left: 0; right: 0; bottom: 0;
    height: 110px;
    background: var(--black);
    color: var(--white);
    font-size: 34px;
    font-weight: 300;
    display: flex;
    align-items: center;
    padding-left: 36px;
  }
  .trainer-photo {
    position: absolute;
    right: 24px; bottom: 0;
    width: 196px; height: 400px;
    background: linear-gradient(180deg, var(--photo-a) 0%, var(--photo-b) 45%, #2a2a2b 100%);
    border-radius: 98px 98px 0 0;
  }
</style>
</head>
<body>
  <section class="card card--front" aria-label="Vorderseite">
    <div class="brand-mark" aria-hidden="true"></div>
    <h1 class="brand-name">Tobias Kellinger</h1>
    <p class="brand-role">Personal Trainer</p>
  </section>

  <section class="card card--back" aria-label="Rückseite">
    <ul class="contact-list">
      <li class="contact-item">
        <svg viewBox="0 0 24 24" aria-hidden="true"><path d="M12 2a7 7 0 0 0-7 7c0 5 7 13 7 13s7-8 7-13a7 7 0 0 0-7-7zm0 9.5A2.5 2.5 0 1 1 12 6.5a2.5 2.5 0 0 1 0 5z"/></svg>
        Lindenfeldweg 14, 80412 München
      </li>
      <li class="contact-item">
        <svg viewBox="0 0 24 24" aria-hidden="true"><path d="M6.6 10.8a15 15 0 0 0 6.6 6.6l2.2-2.2a1 1 0 0 1 1-.25 11.4 11.4 0 0 0 3.6.6 1 1 0 0 1 1 1V20a1 1 0 0 1-1 1A17 17 0 0 1 3 4a1 1 0 0 1 1-1h3.5a1 1 0 0 1 1 1c0 1.25.2 2.45.6 3.6a1 1 0 0 1-.25 1z"/></svg>
        0163/2918374
      </li>
      <li class="contact-item">
        <svg viewBox="0 0 24 24" aria-hidden="true"><path d="M2 5h20v14H2zm2 2v.4l8 5.4 8-5.4V7zm0 2.8V17h16V9.8l-8 5.4z"/></svg>
        t.kellinger@postfeld.de
      </li>
    </ul>
    <div class="web-band">www.tobiaskellinger.de</div>
    <div class="trainer-photo" role="img" aria-label="Schwarz-weiß Porträtfoto des Trainers mit verschränkten Armen"></div>
  </section>
</body>
</html>
```